WebDesign | Financial Services Firm - Risk Mitigation

We are a professional services consulting firm that specializes in high net worth individuals over $25,000,000, executives C-suite and above, closely held businesses owners, family offices and highly compensated employees.

Our focus is on risk mitigation and tax efficient strategies. Our clients take their risk on themselves and have a proven track record generating wealth. Our directive is to preserve and protect the wealth they’ve already created.

Our company Harbinger Collective is geared around five directives of asset protection:
1) Legal Structuring
2) Leverage & Financing
3) Risk Management - Asset Protection & Insurance, Trustee Work
4) Asset Management & Investing - Under www.dvkfarcoast.com
5) Tax Efficient Strategies

Our Company Mark is a Pentagon with a key in the middle. A pentagon is the most efficient defensive structure. Each point of a pentagon is equal distance front every point . Each side provides support to another and works together, which is the key to our clients success.

Our key colors are blue, black and silver.

We ‘re located in the Pacific Northwest with bi coastal and international clients. We have fewer, higher net worth clients and provide exceptional customer service. We do not do social media.

We'll need the following pages:
-Front Landing Page.
Front page has to have link to hcportal.filevaultly.net for logging into secure site.
- Contact & About Us Page
- Our Team Page
- Five Sides of Wealth Management
> Legal & Business Structuring
> Leverage & Financing
> Risk Management & Asset Protection.
> Asset Management and Investing - Will link to DVK (won't be turned on for a few months)
> Tax Efficient Strategies.

Industry/Entity Type

Financial Service

Coding

Coded - Design and coding required

Number of Pages Required

5+ page

Font styles to use
Sans Serif

Colors
0555a3

Requirements
Must have
• Our key colors are blue, black and silver.

-Front Landing Page.
- Contact & About Us Page
- Our Team Page
> Leverage & Financing
Nice to have
• I have attached images that have been purchased for use on the webpage. Us or not.

location page: 872 W Birchwood Ave, Suite 114, Lake Oswego, OR 97035
Should not have
• lots of color.

```html
<!DOCTYPE html>
<html lang="en">
<head>
<meta charset="utf-8">
<title>Harbinger Collective</title>
<link rel="stylesheet" href="https://fonts.googleapis.com/css2?family=Kreon:wght@400;500&family=Lato:ital,wght@0,400;0,700;1,400&display=swap">
<style>
:root{
  --blue:#0555a3;
  --blue-deep:#034688;
  --ink:#2b2f36;
  --text:#6b6f76;
  --dark:#242a33;
  --silver:#c9ced6;
  --light:#f7f7f7;
  --white:#ffffff;
}
html,body{margin:0;padding:0;width:1200px;height:3972px;overflow:hidden;background:var(--white);}
.page{position:relative;width:1200px;height:3972px;overflow:hidden;font-family:"Lato",sans-serif;color:var(--ink);}
.abs{position:absolute;}
.serif{font-family:"Kreon",serif;}
.hero-photo{left:0;top:0;width:1200px;height:850px;background:linear-gradient(180deg,#28303d 0%,#3b3c3d 40%,#4a4036 65%,#2a2b2e 100%);}
.hero-shade{left:0;top:0;width:1200px;height:850px;background:rgba(20,26,38,.35);}
.brand{font-family:"Kreon",serif;font-weight:400;letter-spacing:5px;text-align:center;line-height:1.15;}
.brand-top{left:95px;top:96px;width:230px;color:var(--white);font-size:22px;}
.brand-top .mark{display:block;width:26px;height:26px;border:2px solid var(--white);border-radius:50%;margin:0 auto 12px;}
.nav{left:480px;top:54px;display:flex;gap:0;}
.nav a{font-family:"Kreon",serif;color:var(--white);text-decoration:none;font-size:15px;letter-spacing:.5px;margin-right:60px;}
.hero-title{left:0;width:1200px;top:366px;text-align:center;font-family:"Kreon",serif;color:var(--white);font-size:64px;font-weight:400;margin:0;letter-spacing:1px;}
.hero-sub{left:0;width:1200px;top:460px;text-align:center;font-family:"Kreon",serif;color:var(--white);font-size:20px;margin:0;}
.btn-solid{left:538px;top:505px;width:157px;height:55px;background:var(--blue);color:var(--white);font-family:"Kreon",serif;font-size:17px;display:flex;align-items:center;justify-content:center;text-decoration:none;border-radius:2px;}
.section-title{left:0;width:1200px;text-align:center;font-family:"Kreon",serif;font-weight:400;font-size:40px;color:#3a3d42;margin:0;display:flex;justify-content:center;align-items:center;gap:6px;}
.section-title::before,.section-title::after{content:"";display:block;width:90px;height:3px;background:linear-gradient(90deg,transparent,var(--blue));}
.section-title::after{background:linear-gradient(90deg,var(--blue),transparent);}
.diagram{left:0;top:940px;width:1200px;height:520px;}
.pillar{font-family:"Kreon",serif;font-size:19px;letter-spacing:.8px;color:#3a3d42;text-align:center;line-height:30px;width:320px;}
.core{left:500px;top:1200px;width:200px;height:160px;text-align:center;color:var(--blue);font-size:22px;letter-spacing:3px;}
.core .mark{display:block;width:40px;height:40px;border:3px solid var(--blue);border-radius:50%;margin:0 auto 14px;}
.about-img{left:126px;top:1708px;width:406px;height:343px;background:linear-gradient(135deg,#3a7cc4 0%,#9ab6d3 45%,#b98a62 70%,#2f67a8 100%);opacity:.9;}
.about-title{left:566px;width:492px;top:1720px;color:var(--white);}
.about-title::before,.about-title::after{background:var(--white);}
.about-text{left:566px;top:1790px;width:492px;color:var(--white);font-size:16px;line-height:26.6px;text-align:justify;text-align-last:center;margin:0;}
.btn-ghost{left:739px;top:2025px;width:172px;height:52px;border:2px solid var(--white);color:var(--white);font-family:"Kreon",serif;font-size:19px;display:flex;align-items:center;justify-content:center;text-decoration:none;border-radius:2px;}
.team-bg{left:0;top:2167px;width:1200px;height:683px;background:var(--light);}
.hex{width:213px;height:246px;clip-path:polygon(50% 0,100% 25%,100% 75%,50% 100%,0 75%,0 25%);}
.hex-a{left:236px;top:2321px;background:linear-gradient(160deg,#7b6a5e,#3f4a7a 60%,#5a62c8);}
.hex-b{left:745px;top:2321px;background:linear-gradient(160deg,#7ea65a,#5c6d55 55%,#3a3f4a);}
.quote{width:360px;text-align:center;font-style:italic;font-size:14px;line-height:24px;color:var(--text);margin:0;}
.member{width:360px;text-align:center;}
.member .name{font-family:"Kreon",serif;font-style:italic;color:var(--blue);font-size:20px;display:block;}
.member .role{font-style:italic;color:var(--text);font-size:13.5px;display:block;margin-top:4px;}
.card{width:315px;}
.card-img{width:315px;height:259px;}
.badge{left:20px;top:231px;width:119px;height:39px;background:var(--blue);color:var(--white);font-family:"Kreon",serif;font-size:16px;display:flex;align-items:center;justify-content:center;}
.card-title{font-family:"Kreon",serif;font-size:17px;color:#3a3d42;line-height:28px;margin:42px 0 9px;}
.card-text{font-size:14px;line-height:25px;color:var(--text);margin:0;}
.foot-h{font-family:"Kreon",serif;color:var(--white);font-size:18px;margin:0;letter-spacing:.5px;}
.foot-list{list-style:none;margin:0;padding:0;}
.foot-list li{color:var(--white);font-size:13px;line-height:24px;}
.foot-text{color:var(--white);font-size:13px;line-height:20px;margin:0;}
.email{left:899px;top:3756px;width:190px;height:36px;background:var(--white);border-radius:3px;display:flex;align-items:center;justify-content:space-between;padding:0 10px;box-sizing:border-box;font-size:12px;color:#555;}
.divider{left:111px;top:3897px;width:978px;height:1px;background:#4a505a;}
.copy{left:0;width:1200px;top:3926px;text-align:center;color:var(--white);font-size:12px;}
</style>
</head>
<body>
<div class="page">

  <!-- Hero -->
  <div class="abs hero-photo" role="img" aria-label="Evening view of a stone and timber lodge building with a landscaped plaza"></div>
  <div class="abs hero-shade"></div>
  <div class="abs brand brand-top"><span class="mark"></span>HARBINGER<br>COLLECTIVE</div>
  <nav class="abs nav">
    <a href="#">HOME</a><a href="#">ABOUT US</a><a href="#">OUR TEAM</a><a href="#">SERVICES</a><a href="#" style="margin-right:0">CONTACT US</a>
  </nav>
  <h1 class="abs hero-title">HARBINGER COLLECTIVE</h1>
  <p class="abs hero-sub">At vero eos et accusamus et iusto odio dignissimos ducimus</p>
  <a class="abs btn-solid" href="#">READ MORE</a>
  <svg class="abs" style="left:0;top:700px" width="1200" height="160" viewBox="0 0 1200 160">
    <polygon points="0,130 332,17 1200,140 1200,160 0,160" fill="#fff"/>
    <polyline points="0,130 332,17 1200,140" fill="none" stroke="var(--blue)" stroke-width="5"/>
    <polyline points="0,134 332,24 1200,144" fill="none" stroke="#ffffff" stroke-width="1"/>
  </svg>

  <!-- Wealth management -->
  <h2 class="abs section-title" style="top:856px">WEALTH MANAGEMENT</h2>
  <svg class="abs diagram" viewBox="0 940 1200 520" width="1200" height="520" fill="none" stroke="var(--blue)" stroke-width="1.5">
    <g stroke="var(--blue)" stroke-width="1.5">
      <line x1="600" y1="1103" x2="600" y2="1190"/>
      <polyline points="398,1190 398,1234 500,1234"/>
      <polyline points="800,1196 800,1234 700,1234"/>
      <polyline points="440,1370 440,1330 510,1330"/>
      <polyline points="774,1370 774,1330 690,1330"/>
    </g>
    <g fill="var(--blue)" stroke="none">
      <circle cx="600" cy="1086" r="5"/><circle cx="398" cy="1190" r="5"/><circle cx="800" cy="1196" r="5"/>
      <circle cx="440" cy="1370" r="5"/><circle cx="774" cy="1370" r="5"/>
    </g>
    <!-- document icon -->
    <g stroke="#2b2f36" stroke-width="2">
      <rect x="580" y="967" width="40" height="50" rx="3"/>
      <line x1="588" y1="980" x2="612" y2="980"/><line x1="588" y1="988" x2="612" y2="988"/><line x1="588" y1="996" x2="604" y2="996"/>
      <circle cx="608" cy="1007" r="4" stroke="var(--blue)"/>
    </g>
    <!-- warning + hands -->
    <g stroke="#2b2f36" stroke-width="2">
      <polygon points="256,1087 270,1112 242,1112" stroke="var(--blue)"/>
      <line x1="256" y1="1096" x2="256" y2="1104" stroke="var(--blue)"/>
      <path d="M216 1128 L236 1122 L256 1132 L276 1122 L296 1128 L292 1158 L256 1150 L220 1158 Z"/>
    </g>
    <!-- coins + chart -->
    <g stroke="#2b2f36" stroke-width="2">
      <polyline points="915,1148 930,1135 945,1140 968,1112" stroke="var(--blue)"/>
      <circle cx="968" cy="1112" r="3" stroke="var(--blue)"/>
      <ellipse cx="922" cy="1158" rx="9" ry="4"/><ellipse cx="922" cy="1166" rx="9" ry="4"/>
      <ellipse cx="944" cy="1152" rx="9" ry="4"/><ellipse cx="944" cy="1160" rx="9" ry="4"/><ellipse cx="944" cy="1168" rx="9" ry="4"/>
      <ellipse cx="966" cy="1146" rx="9" ry="4"/><ellipse cx="966" cy="1154" rx="9" ry="4"/><ellipse cx="966" cy="1162" rx="9" ry="4"/><ellipse cx="966" cy="1170" rx="9" ry="4"/>
    </g>
    <!-- flow + gear -->
    <g stroke="#2b2f36" stroke-width="2">
      <rect x="294" y="1316" width="54" height="46"/>
      <rect x="302" y="1340" width="12" height="10" stroke="var(--blue)"/><rect x="326" y="1340" width="12" height="10"/>
      <line x1="314" y1="1345" x2="326" y2="1345"/>
      <circle cx="342" cy="1318" r="12" stroke="var(--blue)"/><circle cx="342" cy="1318" r="4" stroke="var(--blue)"/>
    </g>
    <!-- tax doc -->
    <g stroke="#2b2f36" stroke-width="2">
      <rect x="852" y="1313" width="36" height="48"/>
      <rect x="858" y="1319" width="24" height="12" stroke="var(--blue)"/>
      <line x1="858" y1="1340" x2="880" y2="1340"/><line x1="858" y1="1348" x2="874" y2="1348"/>
      <rect x="882" y="1340" width="20" height="27"/>
    </g>
  </svg>
  <div class="abs pillar" style="left:440px;top:1029px">LEGAL &amp; BUSINESS<br>STRUCTURI</div>
  <div class="abs pillar" style="left:97px;top:1177px">RISK MANAGEMENT &amp;<br>ASSET PROTECTION</div>
  <div class="abs pillar" style="left:785px;top:1181px">LEVERAGE &amp; FINANCING</div>
  <div class="abs pillar" style="left:167px;top:1377px">ASSET MANAGEMENT<br>&amp; INVESTING</div>
  <div class="abs pillar" style="left:718px;top:1377px">TAX EFFICIENT<br>STRATEGIES</div>
  <div class="abs brand core"><span class="mark"></span>HARBINGER<br>COLLECTIVE</div>

  <!-- About -->
  <svg class="abs" style="left:0;top:1495px" width="1200" height="672" viewBox="0 0 1200 672">
    <polygon points="0,16 868,129 1200,16 1200,672 0,672" fill="var(--blue)"/>
    <polyline points="0,6 868,119 1200,4" fill="none" stroke="var(--blue)" stroke-width="2"/>
  </svg>
  <div class="abs about-img" role="img" aria-label="Close-up photograph of stacked coins and banknotes in blue tones"></div>
  <h2 class="abs section-title about-title">ABOUT US</h2>
  <p class="abs about-text">At vero eos et accusamus et iusto odio dignissimos ducimus qui blanditiis praesentium voluptatum deleniti atque corrupti quos dolores et quas molestias excepturi sint occaecati cupiditate non provident, similique sunt in culpa qui officia deserunt mollitia animi, id est laborum et dolorum fuga. Et harum quidem rerum facilis est et expedita distinctio. Nam libero tempore, cum soluta nobis est eligendi optio cumque nihil impedit quo minus id quod maxime placeat facere possimus, omnis voluptas assumenda est</p>
  <a class="abs btn-ghost" href="#">READ MORE</a>

  <!-- Team -->
  <div class="abs team-bg"></div>
  <h2 class="abs section-title" style="top:2230px">OUR TEAM</h2>
  <svg class="abs" style="left:50px;top:2480px" width="30" height="116" viewBox="0 0 30 116"><polyline points="26,2 3,58 26,114" fill="none" stroke="#8a8f96" stroke-width="2"/></svg>
  <svg class="abs" style="left:1130px;top:2480px" width="30" height="116" viewBox="0 0 30 116"><polyline points="4,2 27,58 4,114" fill="none" stroke="#8a8f96" stroke-width="2"/></svg>
  <div class="abs hex hex-a" role="img" aria-label="Portrait of a team member"></div>
  <div class="abs hex hex-b" role="img" aria-label="Portrait of a team member"></div>
  <p class="abs quote" style="left:163px;top:2586px">At vero eos et accusamus et iusto odio dignissimos ducim us qui blanditiis praesentium voluptatum deleniti atque corrupti quos dolores et quas molestias excepturi sint occaecati cupiditate non provident, similique sunt in culpa qui officia deserunt mollitia animi</p>
  <p class="abs quote" style="left:671px;top:2586px">At vero eos et accusamus et iusto odio dignissimos ducim us qui blanditiis praesentium voluptatum deleniti atque corrupti quos dolores et quas molestias excepturi sint occaecati cupiditate non provident, similique sunt in culpa qui officia deserunt mollitia animi</p>
  <div class="abs member" style="left:163px;top:2722px"><span class="name">-Marcus Hale</span><span class="role">At vero eos et accusamus et</span></div>
  <div class="abs member" style="left:671px;top:2722px"><span class="name">-Marcus Hale</span><span class="role">At vero eos et accusamus et</span></div>

  <!-- News -->
  <h2 class="abs section-title" style="top:2916px">RECENT NEWS</h2>
  <article class="abs card" style="left:111px;top:3012px">
    <div class="card-img" role="img" aria-label="Town street corner at dusk with light trails" style="background:linear-gradient(180deg,#3f5fa8 0%,#8a6a8c 45%,#3a3436 80%,#6b6c72 100%)"></div>
    <div class="abs badge">FEB 25,2021</div>
    <h3 class="card-title">At vero eos et accusamus et iusto odio dignissimos ducimus</h3>
    <p class="card-text">Nam libero tempore, cum soluta nobis est elig endi optio cumque nihil impedit quo minus id quod maxime placeat facere possimus</p>
  </article>
  <article class="abs card" style="left:443px;top:3012px">
    <div class="card-img" role="img" aria-label="Stacks of coins on colourful banknotes" style="background:linear-gradient(135deg,#6f8fb8 0%,#c9a27a 40%,#b0584e 70%,#d8c9b4 100%)"></div>
    <div class="abs badge">FEB 25,2021</div>
    <h3 class="card-title">At vero eos et accusamus et iusto odio dignissimos ducimus</h3>
    <p class="card-text">Nam libero tempore, cum soluta nobis est elig endi optio cumque nihil impedit quo minus id quod maxime placeat facere possimus</p>
  </article>
  <article class="abs card" style="left:774px;top:3012px">
    <div class="card-img" role="img" aria-label="Stone and timber lodge building under a blue sky" style="background:linear-gradient(180deg,#4f8fd6 0%,#a9c6e4 35%,#6a5a4c 65%,#4a4540 100%)"></div>
    <div class="abs badge">FEB 25,2021</div>
    <h3 class="card-title">At vero eos et accusamus et iusto odio dignissimos ducimus</h3>
    <p class="card-text">Nam libero tempore, cum soluta nobis est elig endi optio cumque nihil impedit quo minus id quod maxime placeat facere possimus</p>
  </article>

  <!-- Footer -->
  <svg class="abs" style="left:0;top:3478px" width="1200" height="494" viewBox="0 0 1200 494">
    <polygon points="0,10 332,126 1200,4 1200,494 0,494" fill="var(--dark)"/>
    <polyline points="0,18 332,134 1200,12" fill="none" stroke="var(--blue)" stroke-width="4"/>
  </svg>
  <div class="abs brand" style="left:172px;top:3714px;width:260px;color:var(--white);font-size:26px"><span style="display:block;width:30px;height:30px;border:2px solid var(--white);border-radius:50%;margin:0 auto 14px"></span>HARBINGER<br>COLLECTIVE</div>
  <div class="abs" style="left:480px;top:3658px">
    <h4 class="foot-h">MENU</h4>
    <ul class="foot-list" style="margin-top:14px"><li>HOME</li><li>ABOUT US</li><li>OUR TEAM</li><li>SERVICES</li><li>CONTACT US</li></ul>
  </div>
  <div class="abs" style="left:663px;top:3658px">
    <h4 class="foot-h">CONTACT</h4>
    <div style="display:flex;gap:12px;margin-top:20px">
      <svg width="24" height="24" viewBox="0 0 24 24"><circle cx="12" cy="12" r="12" fill="#fff"/><path d="M12 6a4 4 0 0 0-4 4c0 3 4 8 4 8s4-5 4-8a4 4 0 0 0-4-4z" fill="var(--dark)"/><circle cx="12" cy="10" r="1.5" fill="#fff"/></svg>
      <p class="foot-text">1458 Dummy Text<br>lorem, CA 91710</p>
    </div>
    <div style="display:flex;gap:12px;margin-top:12px">
      <svg width="24" height="24" viewBox="0 0 24 24"><circle cx="12" cy="12" r="12" fill="#fff"/><rect x="6" y="8" width="12" height="8" fill="var(--dark)"/><polyline points="6,8 12,13 18,8" fill="none" stroke="#fff" stroke-width="1"/></svg>
      <p class="foot-text">E mail Us<br>info@company.com</p>
    </div>
  </div>
  <div class="abs" style="left:899px;top:3658px">
    <h4 class="foot-h">FOLLOW US</h4>
    <p class="foot-text" style="margin-top:16px;width:180px">At vero eos et accusamus et iusto odio dignissimos</p>
  </div>
  <div class="abs email"><span>Email :</span><svg width="14" height="14" viewBox="0 0 14 14"><polygon points="1,7 13,1 9,13 7,8" fill="none" stroke="var(--blue)" stroke-width="1.5"/></svg></div>
  <div class="abs divider"></div>
  <div class="abs copy">Copyright © 2021 All Rights Reserved</div>
</div>
</body>
</html>
```